Pig Roasting for all occasions

I am looking for a pig picture or something to get my concept going before you even start to read the details.
This design I will use for everything. T shirts, Thank You cards, etc
Perhaps something to go along with the Name. There are other
Hog Marauder picture web sites out there but I don't like any of there pictures. And for that matter I don't want to copy them any way.

My main business is Pig Roasting but I do a lot of catering along with it. I will be doing a lot of sausage (Wurst) with the pig roast
hence " Grill Fellows"
I also do beef and chicken but the main stay is Pork

Target Market(s)

For the backyard or Corporate Party - Target 50 + People

Industry/Entity Type

Catering

Contact Information for Business Card

The Hog Marauder BBQ
Pig roasting for all occasions
Grill Fellows
THEHOGMARAUDERBBQ.EXAMPLE
Dale Fenwicke
4127 Larchmont Dr
Indian Trail, NC 28079
(555) 273 - 6648
thehogmarauderbbq@mailbox.example

```html
<!DOCTYPE html>
<html lang="en">
<head>
<meta charset="utf-8">
<title>The Hog Marauder BBQ – Business Card</title>
<link rel="stylesheet" href="https://fonts.googleapis.com/css2?family=Varela+Round&family=Signika:wght@500;600&family=Open+Sans:ital,wght@1,700&display=swap">
<style>
  :root {
    --stage: #8e8e8e;
    --ember-dark: #2a0306;
    --roast-orange: #e8632b;
    --roast-brown: #7a2a14;
    --deep-brown: #5a1a10;
    --paper: #ffffff;
  }
  html, body {
    margin: 0;
    padding: 0;
    width: 1200px;
    height: 1200px;
    overflow: hidden;
    background: var(--stage);
  }
  .card {
    position: absolute;
    left: 27px;
    top: 266px;
    width: 1146px;
    height: 669px;
    background: var(--paper);
    overflow: hidden;
  }
  .contact-panel {
    position: absolute;
    left: 0;
    top: 0;
    width: 670px;
    height: 100%;
    background: var(--ember-dark);
  }
  .flame-edge {
    position: absolute;
    left: 640px;
    top: 0;
    width: 100px;
    height: 100%;
    background: linear-gradient(to right, var(--ember-dark) 0%, var(--ember-dark) 30%, #7a5a5b 60%, var(--paper) 100%);
  }
  .contact {
    position: absolute;
    left: 45px;
    font-family: "Varela Round", sans-serif;
    white-space: nowrap;
    margin: 0;
  }
  .contact-web {
    top: 140px;
    font-size: 29px;
    color: var(--roast-orange);
    letter-spacing: 0.5px;
  }
  .contact-details {
    top: 225px;
    font-size: 31px;
    line-height: 66px;
    color: var(--paper);
    font-style: normal;
  }
  .contact-email {
    top: 498px;
    font-size: 25px;
    color: var(--roast-orange);
  }
  .brand-mark {
    position: absolute;
    left: 790px;
    top: 95px;
    width: 300px;
    height: 260px;
    display: flex;
    flex-direction: column;
    align-items: center;
    justify-content: center;
    gap: 22px;
  }
  .brand-dot {
    width: 90px;
    height: 90px;
    border-radius: 50%;
    background: var(--roast-orange);
  }
  .brand-name {
    font-family: "Varela Round", sans-serif;
    font-size: 36px;
    color: var(--roast-brown);
    white-space: nowrap;
  }
  .service-title {
    position: absolute;
    left: 720px;
    top: 340px;
    margin: 0;
    font-family: "Signika", sans-serif;
    font-weight: 600;
    font-size: 64px;
    line-height: 1;
    color: var(--deep-brown);
    white-space: nowrap;
  }
  .service-subtitle {
    position: absolute;
    left: 722px;
    top: 420px;
    margin: 0;
    font-family: "Signika", sans-serif;
    font-weight: 500;
    font-size: 41px;
    line-height: 1;
    color: var(--roast-orange);
    white-space: nowrap;
  }
  .slogan {
    position: absolute;
    left: 755px;
    top: 512px;
    margin: 0;
    font-family: "Open Sans", sans-serif;
    font-style: italic;
    font-weight: 700;
    font-size: 33px;
    letter-spacing: 2.5px;
    color: var(--roast-brown);
    white-space: nowrap;
  }
</style>
</head>
<body>
  <div class="card">
    <div class="contact-panel"></div>
    <div class="flame-edge" role="img" aria-label="Decorative white flame border between the dark contact panel and the white logo side"></div>

    <p class="contact contact-web">THEHOGMARAUDERBBQ.EXAMPLE</p>
    <address class="contact contact-details">
      Dale Fenwicke,<br>
      4127 Larchmont Dr Indian Trail,<br>
      NC 28079,<br>
      (555) 273 - 6648
    </address>
    <p class="contact contact-email">thehogmarauderbbq@mailbox.example</p>

    <div class="brand-mark">
      <span class="brand-dot"></span>
      <span class="brand-name">Hog Marauder</span>
    </div>

    <h1 class="service-title">Pig Roasting</h1>
    <p class="service-subtitle">For All Occasions</p>
    <p class="slogan">Grill Fellows</p>
  </div>
</body>
</html>
```